BrightLane Real Estate Sign

We are in the process of rebranding our business and need a new For Sale \ Sold sign.
We're a prestige real estate agency and therefore require a really stylish sign.
I've uploaded the following files
1. The new company logo
2. "sample sign.jpg" which shows the type of sign we would like. It is a metal sign with a top panel and bottom panel.
3. Our previous sign "previous sign.jpg" if you're interested in seeing it.
The sign must be black with white text.
Our thoughts are that the top panel (refer to sample sign) would contain the text "For Sale" or "Sold". These would be two separate panels which are interchangeable and could be screwed in place.
The bottom panel would not contain any photos like the sample. However, it may contain our logo and my contact details etc.
The sign is 900mm wide x 1200mm high.
My details are:
Name: Desmond Harlow
Web: www.blrealestate.com.au
Email: sales@blrealestate.com.au
Phone: 0491 836 205

```html
<!DOCTYPE html>
<html lang="en">
<head>
<meta charset="utf-8">
<title>BrightLane Real Estate – For Sale Sign</title>
<link href="https://fonts.googleapis.com/css2?family=Open+Sans:wght@400;600;700&display=swap" rel="stylesheet">
<style>
  :root {
    --backdrop: #e9ebe8;
    --post: #1c1c1c;
    --panel-grey: #6d706e;
    --panel-black: #0e0e0e;
    --sign-white: #f7f7f7;
    --ink: #141414;
    --text-white: #ffffff;
  }
  html, body {
    margin: 0;
    padding: 0;
    overflow: hidden;
  }
  body {
    width: 1200px;
    height: 900px;
    background: var(--backdrop);
    font-family: "Open Sans", Arial, sans-serif;
    position: relative;
  }
  .sign {
    position: absolute;
    left: 300px;
    top: 26px;
    width: 595px;
    height: 848px;
  }
  .post {
    position: absolute;
    top: 0;
    width: 24px;
    height: 848px;
    background: var(--post);
  }
  .post--left { left: 0; }
  .post--right { right: 0; }
  .header-panel {
    position: absolute;
    left: 0;
    top: 0;
    width: 595px;
    height: 251px;
    background: linear-gradient(to bottom, var(--panel-grey) 0 120px, var(--panel-black) 120px 100%);
    display: flex;
    align-items: flex-start;
    justify-content: center;
  }
  .header-panel__title {
    margin: 62px 0 0;
    color: var(--text-white);
    font-weight: 700;
    font-size: 106px;
    line-height: 1;
    letter-spacing: 1px;
  }
  .info-panel {
    position: absolute;
    left: 30px;
    top: 272px;
    width: 546px;
    height: 475px;
    background: var(--sign-white);
  }
  .brand {
    position: absolute;
    left: 40px;
    top: 110px;
    display: flex;
    align-items: center;
    gap: 28px;
  }
  .brand__mark {
    width: 70px;
    height: 70px;
    background: var(--ink);
  }
  .brand__name {
    color: var(--ink);
    font-weight: 700;
    font-size: 58px;
    line-height: 1;
    letter-spacing: -0.5px;
  }
  .contact {
    position: absolute;
    left: 10px;
    top: 322px;
    margin: 0;
    padding: 0;
    list-style: none;
  }
  .contact__row {
    height: 36px;
    display: flex;
    align-items: center;
    padding: 0 14px 0 30px;
    font-size: 26px;
    color: var(--ink);
    width: max-content;
  }
  .contact__row--band {
    background: var(--panel-black);
    color: var(--text-white);
  }
</style>
</head>
<body>
  <div class="sign">
    <div class="post post--left"></div>
    <div class="post post--right"></div>

    <div class="header-panel">
      <h1 class="header-panel__title">FOR SALE</h1>
    </div>

    <div class="info-panel">
      <div class="brand">
        <div class="brand__mark"></div>
        <div class="brand__name">BrightLane</div>
      </div>

      <ul class="contact">
        <li class="contact__row contact__row--band">Desmond Harlow</li>
        <li class="contact__row">Web: www.blrealestate.com.au</li>
        <li class="contact__row contact__row--band">Email: sales@blrealestate.com.au</li>
        <li class="contact__row">Phone: 0491 836 205</li>
      </ul>
    </div>
  </div>
</body>
</html>
```